Brochure design for BRAVACARE clinic

We are seeking for a brochure design for new medical walk-in clinic.
The desirable design for the brochure will contain strong concept of positioning for
" convenience" of medical care in terms of access, affordability and service.
I am looking forward to having eye-catching modern design.
Updates

 I've updated the logo file to ai file

and for your reference please see our web page www.brava-care.example
to keep consistency in terms of  color scheme  and impression

Thanks

Dear Designers,

We'd like to make the deadline earlier by Dec 17(Tuesday) 
Thank you..

Target Market(s)

Age from 20 - 50

Industry/Entity Type

Medical

Colors
f78f20
33a6d7

Requirements
Must have
• Multi-language greeting line in Korean, Chinese, Japanese and English on the cover page.

8 x11.7 sized tri-fold
Nice to have
• Please refer to our web page in order to keep consistency
www.brava-care.example

```html
<!DOCTYPE html>
<html lang="en">
<head>
<meta charset="utf-8">
<title>BRAVACARE Brochure Cover</title>
<link rel="stylesheet" href="https://fonts.googleapis.com/css2?family=Didact+Gothic&family=Noto+Sans+KR:wght@400;500&family=Noto+Sans+JP:wght@400&family=Noto+Sans+SC:wght@500&display=swap">
<style>
  :root {
    --navy-deep: #0f2a40;
    --navy-mid: #163a57;
    --navy-glow: #1d4a6c;
    --brand-red: #a81f24;
    --text-red: #c3262b;
    --white: #ffffff;
    --soft-grey: #cfd6dd;
  }
  html, body {
    margin: 0;
    padding: 0;
    width: 1200px;
    height: 848px;
    overflow: hidden;
  }
  .cover {
    position: relative;
    width: 1200px;
    height: 848px;
    overflow: hidden;
    background:
      radial-gradient(ellipse 420px 360px at 1010px 390px, var(--navy-glow) 0%, rgba(29,74,108,0) 100%),
      linear-gradient(180deg, var(--navy-mid) 0%, var(--navy-deep) 100%);
    font-family: "Didact Gothic", "Century Gothic", sans-serif;
  }
  .brand {
    position: absolute;
    right: 78px;
    top: 418px;
    display: flex;
    align-items: center;
    gap: 14px;
  }
  .brand-square {
    width: 22px;
    height: 22px;
    background: var(--brand-red);
  }
  .brand-name {
    color: var(--white);
    font-size: 40px;
    line-height: 1;
    letter-spacing: -0.5px;
  }
  .band {
    position: absolute;
    top: 661px;
    height: 111px;
    background: var(--brand-red);
  }
  .band-left { left: 0; width: 44px; }
  .band-center { left: 352px; width: 576px; }
  .band-right { left: 1177px; width: 23px; }
  .contact {
    position: absolute;
    left: 66px;
    top: 666px;
    width: 262px;
    font-size: 15px;
    line-height: 18px;
  }
  .contact-row {
    display: flex;
    justify-content: space-between;
  }
  .contact-label { color: var(--text-red); }
  .contact-value {
    color: var(--white);
    font-style: italic;
    text-align: right;
  }
  .contact-value .accent { color: var(--text-red); }
  .greeting {
    position: absolute;
    left: 937px;
    top: 664px;
    width: 228px;
  }
  .greeting-line {
    margin: 0;
    text-align: justify;
    text-align-last: justify;
    white-space: nowrap;
    line-height: 24px;
  }
  .greeting-en { color: var(--text-red); font-size: 19px; }
  .greeting-ko { color: var(--white); font-family: "Noto Sans KR", sans-serif; font-size: 18px; }
  .greeting-ja { color: var(--text-red); font-family: "Noto Sans JP", sans-serif; font-size: 18px; }
  .greeting-zh { color: var(--white); font-family: "Noto Sans SC", sans-serif; font-weight: 500; font-size: 18px; }
</style>
</head>
<body>
  <main class="cover">
    <div class="brand">
      <span class="brand-square"></span>
      <span class="brand-name">BRAVACARE</span>
    </div>

    <div class="band band-left"></div>
    <div class="band band-center"></div>
    <div class="band band-right"></div>

    <address class="contact" style="font-style:normal">
      <div class="contact-row"><span class="contact-label">Contact Details:</span><span class="contact-value">418 Linden Park Ave.</span></div>
      <div class="contact-row"><span class="contact-label"></span><span class="contact-value">Fairview, MI 48000</span></div>
      <div class="contact-row"><span class="contact-label">phone:</span><span class="contact-value">+1.555.010.2468</span></div>
      <div class="contact-row"><span class="contact-label">website:</span><span class="contact-value">www.brava-<span class="accent">care</span>.example</span></div>
      <div class="contact-row"><span class="contact-label">e-mail:</span><span class="contact-value">hello@brava-care.example</span></div>
    </address>

    <div class="greeting">
      <p class="greeting-line greeting-en" lang="en">Convenience we value</p>
      <p class="greeting-line greeting-ko" lang="ko">우리가 가치를 편리</p>
      <p class="greeting-line greeting-ja" lang="ja">私たちは大切に利便性</p>
      <p class="greeting-line greeting-zh" lang="zh">方 便 我 们 重 视</p>
    </div>
  </main>
</body>
</html>
```